Relationship Seminar

I am an Author and Speaker and I need a flyer for a Christian relationship seminar targeting women aged between mid 20's to late 30's. It's an event for women only.

-I am looking for a fresh/ edgy look but still feminine
-Nothing too girly
-Maximum of 3 colours (Spring colours are good)
-I want the flyer to convey joy or happiness
-Use my photo which is attached as the predominant image (you can crop it to remove the background etc)

The Flyer Details are as follows:

Somewhere Along The Way - Brisbane Tour

Join Author & Speaker, Rosalind Kupferle, as she speaks about her new book entitled 'Somewhere Along The Way'.

Be inspired and encouraged to embrace the life that God has given you and make the most of it!

Date: Saturday 9th November 2013
Time: 2:00 pm - 5:00 pm
Location: Harwick Lodge Brisbane (Juniper Hall)
Pelham Crescent, Brisbane QLD 4000
Tickets: $60/pp (Includes High Tea)
Buy Tickets: www.rosalindkupferle.com or http://somewherealongtheway.ticketquarry.net

Email: info@rosalindkupferle.com

Include the cover of my new book.

www.rosalindkupferle.com (include my website at the bottom of the flyer)

Target Market(s)

Young professional women aged between their mid 20's to late 30's

Industry/Entity Type

Event

Requirements
Should not have
• -No girly or curly font

```html
<!DOCTYPE html>
<html lang="en">
<head>
<meta charset="utf-8">
<title>Somewhere Along The Way – Brisbane Tour</title>
<link href="https://fonts.googleapis.com/css2?family=Didact+Gothic&family=Open+Sans:wght@400;600;700&display=swap" rel="stylesheet">
<style>
  :root {
    --amber-deep: #e08a2a;
    --amber: #f0a83c;
    --sun: #f7cd5c;
    --sun-pale: #fbe08a;
    --brick-light: #efd2b8;
    --brick: #d9a27c;
    --portrait-light: #8a5a3c;
    --portrait-dark: #3a2418;
    --cream: #fff6dc;
    --white: #ffffff;
    --quote-bg: rgba(150, 84, 40, 0.78);
  }
  * { margin: 0; padding: 0; box-sizing: border-box; }
  html, body { width: 928px; height: 1200px; overflow: hidden; }
  body { background: var(--amber); }

  .flyer {
    position: relative;
    width: 928px;
    height: 1200px;
    overflow: hidden;
    color: var(--white);
    font-family: "Open Sans", Arial, sans-serif;
    background:
      radial-gradient(ellipse at 25% 20%, rgba(255,230,160,0.55), transparent 55%),
      radial-gradient(ellipse at 80% 35%, rgba(255,220,130,0.45), transparent 50%),
      linear-gradient(180deg, var(--amber-deep) 0%, var(--amber) 22%, var(--sun) 36%, var(--amber) 80%, var(--sun) 100%);
  }

  .site-strip {
    position: absolute; left: 0; top: 0; width: 100%; height: 54px;
    background: linear-gradient(90deg, rgba(251,224,138,0.55), rgba(255,236,170,0.85), rgba(251,224,138,0.55));
    display: flex; align-items: center; justify-content: center;
    font-family: "Didact Gothic", sans-serif; font-size: 24px; letter-spacing: 0.5px;
  }

  .event-title {
    position: absolute; left: 0; top: 118px; width: 100%;
    text-align: center;
    font-family: "Didact Gothic", sans-serif; font-weight: 400;
    font-size: 57px; letter-spacing: 0.5px; line-height: 1;
  }
  .title-rule {
    position: absolute; left: 72px; top: 188px; width: 792px; height: 1px;
    background: rgba(255,255,255,0.55);
  }
  .tour-name {
    position: absolute; right: 158px; top: 198px;
    font-family: "Didact Gothic", sans-serif; font-size: 31px; letter-spacing: 0.5px;
  }

  .intro {
    position: absolute; left: 0; top: 282px; width: 100%;
    text-align: center; font-size: 29px; line-height: 40px;
    text-shadow: 0 1px 3px rgba(140,70,10,0.35);
  }
  .intro strong { font-weight: 700; }

  .photo-band {
    position: absolute; left: 0; top: 426px; width: 100%; height: 534px;
    background: linear-gradient(90deg, var(--brick-light) 0%, var(--brick) 50%, var(--brick-light) 100%);
  }

  .author-portrait {
    position: absolute; left: 468px; top: 426px; width: 396px; height: 534px;
    background: linear-gradient(180deg, var(--portrait-light) 0%, var(--portrait-dark) 100%);
  }

  .book-cover {
    position: absolute; left: 74px; top: 456px; width: 222px; height: 484px;
    background: linear-gradient(180deg, #fbfbf8 0%, #eeeee8 78%, #9fcf8e 100%);
    box-shadow: 6px 8px 14px rgba(80,40,20,0.35);
    border-left: 14px solid #e9e7df;
  }

  .tagline {
    position: absolute; left: 358px; top: 838px; width: 570px; height: 88px;
    background: var(--quote-bg);
    padding: 12px 14px 0 18px;
    font-size: 21px; line-height: 31px;
    text-align: right;
  }

  .details {
    position: absolute; left: 84px; top: 964px;
    font-weight: 700; font-size: 19px; line-height: 25px;
    color: var(--cream);
    list-style: none;
  }

  .contact-email {
    position: absolute; right: 10px; top: 1078px;
    font-weight: 700; font-size: 23px; color: var(--cream);
  }

  .ticket-bar {
    position: absolute; left: 0; top: 1116px; width: 100%; height: 84px;
    background: linear-gradient(90deg, rgba(224,138,42,0.75), rgba(240,168,60,0.75));
    padding: 10px 0 0 17px;
    font-weight: 700; font-size: 21px; line-height: 32px;
  }
  .ticket-links { display: flex; gap: 12px; white-space: nowrap; letter-spacing: -0.2px; }
</style>
</head>
<body>
<main class="flyer">
  <div class="site-strip">www.rosalindkupferle.com</div>

  <h1 class="event-title">SOMEWHERE ALONG THE WAY</h1>
  <div class="title-rule"></div>
  <div class="tour-name">BRISBANE TOUR</div>

  <p class="intro">
    Join Author &amp; Speaker, <strong>Rosalind Kupferle,</strong><br>
    as she speaks about her new book<br>
    entitled '<strong>Somewhere Along The Way</strong>'.
  </p>

  <div class="photo-band" role="img" aria-label="Whitewashed brick wall backdrop"></div>
  <div class="author-portrait" role="img" aria-label="Portrait photograph of the smiling author with long dark hair in a dark jacket"></div>
  <div class="book-cover" role="img" aria-label="Cover of the book Somewhere Along The Way by Rosalind Kupferle"></div>

  <p class="tagline">Be inspired and encouraged to embrace the life<br>that God has given you and make the most of it!</p>

  <ul class="details">
    <li>Date: Saturday 9th November 2013</li>
    <li>Time: 2:00 pm - 5:00 pm</li>
    <li>Location: Harwick Lodge Brisbane (Juniper Hall)</li>
    <li>Pelham Crescent, Brisbane QLD 4000</li>
    <li>Tickets: $60/pp (Includes High Tea)</li>
  </ul>

  <div class="contact-email">Email: info@rosalindkupferle.com</div>

  <div class="ticket-bar">
    <div>BUY TICKETS:</div>
    <div class="ticket-links">
      <span>www.rosalindkupferle.com</span>
      <span>•</span>
      <span>http://somewherealongtheway.ticketquarry.net</span>
    </div>
  </div>
</main>
</body>
</html>
```